Rocket business card

Modern business card design, use of color is good with clean space too.

Things to include on card:

Quote: I add fuel to your optometry practice

- Eyewear Sales
- Admin Duties
- Revenue Collection
- Leadership
- Tech Adoption
- COGS Reduction
- Product Sourcing
-Medical Growth

Dalton Vessey, CEO
Glint Harbor
Text Me! 847-302-1964
dalton@glintharbor.example

```html
<!DOCTYPE html>
<html lang="en">
<head>
<meta charset="utf-8">
<title>Glint Harbor – Business Card</title>
<link rel="stylesheet" href="https://fonts.googleapis.com/css2?family=Raleway:wght@400;500;600&display=swap">
<style>
  :root {
    --bg: #e9e9e9;
    --red: #dc3b30;
    --ink: #111111;
    --orange: #e8462a;
    --orange-soft: #f4a13a;
    --white: #ffffff;
    --faint: #fbe9de;
  }
  * { margin: 0; padding: 0; box-sizing: border-box; }
  html, body { width: 1200px; height: 913px; overflow: hidden; background: var(--bg); }
  body { position: relative; font-family: "Raleway", sans-serif; color: var(--ink); }

  .card {
    position: absolute;
    width: 580px; height: 331px;
    border-radius: 18px;
    overflow: hidden;
    box-shadow: 0 6px 18px rgba(0,0,0,.12);
  }

  /* Front */
  .card-front { left: 70px; top: 90px; background: var(--red); }
  .front-brand {
    position: absolute; left: 0; right: 0; top: 70px;
    display: flex; flex-direction: column; align-items: center; gap: 22px;
  }
  .brand-dot {
    width: 78px; height: 78px; border-radius: 50%;
    background: linear-gradient(135deg, var(--orange-soft), var(--orange));
    border: 6px solid var(--white);
  }
  .brand-name {
    font-weight: 600; font-size: 52px; letter-spacing: 2px;
    text-transform: uppercase; color: var(--ink); line-height: 1;
  }
  .tagline {
    position: absolute; left: 0; right: 0; top: 262px;
    text-align: center; font-size: 19px; font-weight: 500;
    letter-spacing: .5px; text-transform: uppercase; color: var(--ink);
  }

  /* Back */
  .card-back { left: 550px; top: 470px; background: var(--white); }
  .back-decor {
    position: absolute; left: 285px; top: 120px;
    width: 160px; height: 160px; border-radius: 50%;
    background: var(--faint);
  }
  .back-brand {
    position: absolute; left: 34px; top: 32px;
    display: flex; flex-direction: column; align-items: flex-start; gap: 14px;
  }
  .back-brand .brand-dot { width: 54px; height: 54px; border-width: 4px; }
  .back-brand .brand-name { font-size: 30px; letter-spacing: 1.5px; }

  .person { position: absolute; left: 50px; top: 178px; }
  .person-name {
    font-size: 24px; font-weight: 500; text-transform: uppercase;
    color: var(--orange); letter-spacing: .5px;
  }
  .person-title { font-size: 12px; text-transform: uppercase; margin-top: 2px; }
  .contact {
    position: absolute; left: 50px; top: 262px;
    font-size: 14px; text-transform: uppercase; line-height: 1.45; letter-spacing: .3px;
  }

  .services {
    position: absolute; right: 30px; top: 34px;
    text-align: right; list-style: none;
  }
  .services-title {
    display: inline-block; color: var(--orange);
    font-size: 16px; text-transform: uppercase; font-weight: 500;
    border-bottom: 2px solid var(--orange); padding-bottom: 1px; margin-bottom: 6px;
    margin-right: 22px;
  }
  .service {
    display: flex; justify-content: flex-end; align-items: center; gap: 8px;
    font-size: 14px; text-transform: uppercase; line-height: 1.5; letter-spacing: .3px;
  }
  .service::after {
    content: ""; width: 12px; height: 12px; border-radius: 50%;
    background: linear-gradient(135deg, var(--orange-soft), var(--orange));
  }
</style>
</head>
<body>
  <section class="card card-front">
    <div class="front-brand">
      <span class="brand-dot"></span>
      <span class="brand-name">Glint Harbor</span>
    </div>
    <p class="tagline">I add fuel to your optometry practice</p>
  </section>

  <section class="card card-back">
    <div class="back-decor" role="img" aria-label="Faint brand emblem decoration"></div>
    <div class="back-brand">
      <span class="brand-dot"></span>
      <span class="brand-name">Glint Harbor</span>
    </div>
    <div class="person">
      <p class="person-name">Dalton Vessey</p>
      <p class="person-title">CEO</p>
    </div>
    <p class="contact">Text me! 847-302-1964<br>dalton@glintharbor.example</p>
    <div class="services">
      <p class="services-title">Our Services</p>
      <ul>
        <li class="service">Eyewear Sales</li>
        <li class="service">Admin Duties</li>
        <li class="service">Revenue Collection</li>
        <li class="service">Leadership</li>
        <li class="service">Tech Adoption</li>
        <li class="service">COGS Reduction</li>
        <li class="service">Product Sourcing</li>
        <li class="service">Medical Growth</li>
      </ul>
    </div>
  </section>
</body>
</html>
```